Ostrel Appraisals BV business cards (a financial services company)

I am looking for a business card design that stands out in the financial advisory field of business & intellectual property valuation. The business card design should be conservative, yet different. Address details have changed since the attached business card. New address is:

Molenvlietkade 27
4817 KT Leiden
The Netherlands

Telephone number remains the same.

```html
<!DOCTYPE html>
<html lang="en">
<head>
<meta charset="utf-8">
<title>Ostrel Appraisals BV – Business Cards</title>
<link rel="stylesheet" href="https://fonts.googleapis.com/css2?family=Questrial&family=Montserrat:wght@400;600&display=swap">
<style>
  :root {
    --backdrop: #1c1c1c;
    --ink: #111111;
    --card-dark: #262324;
    --paper: #f7f7f7;
    --line-light: #e8e8e8;
    --strip-grey: #c9c9c9;
    --bar-grey: #9a9a9a;
    --text-dark: #1a1a1a;
    --text-mid: #444444;
  }
  * { box-sizing: border-box; margin: 0; padding: 0; }
  html, body { width: 1200px; height: 900px; overflow: hidden; }
  body {
    background: var(--backdrop);
    position: relative;
    font-family: "Questrial", sans-serif;
  }
  .card {
    position: absolute;
    width: 560px;
    height: 320px;
    box-shadow: 0 14px 30px rgba(0,0,0,.55);
    overflow: hidden;
  }

  /* Front (dark) card */
  .card-front { left: 110px; top: 80px; background: var(--card-dark); }
  .front-frame {
    position: absolute; inset: 16px;
    border: 1px solid var(--line-light);
  }
  .front-url {
    position: absolute; left: 50%; bottom: 6px; transform: translateX(-50%);
    background: var(--card-dark); padding: 0 14px;
    color: var(--line-light); font-size: 14px; letter-spacing: 3px;
    white-space: nowrap;
  }
  .brand {
    position: absolute; left: 50%; top: 50%; transform: translate(-50%, -50%);
    display: flex; align-items: center; gap: 12px; white-space: nowrap;
  }
  .brand-mark { width: 16px; height: 16px; }
  .brand-name { font-size: 30px; letter-spacing: 1px; text-transform: uppercase; }
  .card-front .brand-mark { background: var(--line-light); }
  .card-front .brand-name { color: var(--line-light); }

  /* Back (white) card */
  .card-back { left: 530px; top: 490px; background: var(--paper); }
  .card-back .brand { top: 92px; }
  .card-back .brand-mark { background: var(--ink); }
  .card-back .brand-name { color: var(--ink); font-size: 28px; }

  .person {
    position: absolute; right: 30px; top: 150px;
    text-align: right; padding-right: 12px;
    border-right: 3px solid var(--bar-grey);
    font-family: "Montserrat", sans-serif;
  }
  .person-name { font-size: 16px; color: var(--text-dark); }
  .person-name strong { font-weight: 600; }
  .person-creds { font-size: 10px; color: var(--text-mid); }
  .person-role { font-size: 10px; color: var(--text-mid); margin-top: 2px; }

  .contact-tab {
    position: absolute; left: 0; bottom: 0; width: 34px; height: 112px;
    background: var(--ink); border-top-right-radius: 12px;
    display: flex; flex-direction: column; justify-content: space-evenly; align-items: center;
    padding: 8px 0;
  }
  .contact-tab svg { width: 14px; height: 14px; }
  .contact-list {
    position: absolute; left: 48px; bottom: 18px; list-style: none;
    font-family: "Montserrat", sans-serif; font-size: 11.5px; color: var(--text-dark);
    line-height: 24px;
  }
  .card-base { position: absolute; left: 0; bottom: 0; }
</style>
</head>
<body>

<section class="card card-front" aria-label="Front of business card">
  <div class="front-frame"></div>
  <div class="brand">
    <span class="brand-mark"></span>
    <span class="brand-name">Ostrel Appraisals</span>
  </div>
  <p class="front-url">www.ostrelappraisals.com</p>
</section>

<section class="card card-back" aria-label="Back of business card">
  <svg class="card-base" width="560" height="320" viewBox="0 0 560 320" aria-hidden="true">
    <path d="M34 320 V300 H370 V320 Z" fill="var(--strip-grey)"/>
    <path d="M370 320 V262 Q370 240 392 238 L560 238 V320 Z" fill="var(--strip-grey)"/>
    <path d="M378 320 V266 Q378 246 398 244 L560 244 V320 Z" fill="var(--ink)"/>
  </svg>

  <div class="brand">
    <span class="brand-mark"></span>
    <span class="brand-name">Ostrel Appraisals</span>
  </div>

  <div class="person">
    <p class="person-name">Maarten <strong>Veldhuis</strong> <span class="person-creds">CFA, ASA, RV</span></p>
    <p class="person-role">Managing Director</p>
  </div>

  <div class="contact-tab" aria-hidden="true">
    <svg viewBox="0 0 24 24"><path fill="#fff" d="M6.6 10.8a15 15 0 0 0 6.6 6.6l2.2-2.2a1 1 0 0 1 1-.25 11.4 11.4 0 0 0 3.6.57 1 1 0 0 1 1 1V20a1 1 0 0 1-1 1A17 17 0 0 1 3 4a1 1 0 0 1 1-1h3.5a1 1 0 0 1 1 1c0 1.25.2 2.45.57 3.57a1 1 0 0 1-.25 1z"/></svg>
    <svg viewBox="0 0 24 24"><path fill="#fff" d="M3 5h18v14H3z"/><path d="M3 5l9 7 9-7" fill="none" stroke="#111" stroke-width="1.6"/></svg>
    <svg viewBox="0 0 24 24" fill="none" stroke="#fff" stroke-width="1.6"><circle cx="12" cy="12" r="9"/><ellipse cx="12" cy="12" rx="4" ry="9"/><path d="M3 12h18M5 7h14M5 17h14"/></svg>
    <svg viewBox="0 0 24 24"><path fill="#fff" d="M12 2a7 7 0 0 0-7 7c0 5 7 13 7 13s7-8 7-13a7 7 0 0 0-7-7zm0 9.5A2.5 2.5 0 1 1 12 6.5a2.5 2.5 0 0 1 0 5z"/></svg>
  </div>

  <ul class="contact-list">
    <li>+31 (0)70 348 1926</li>
    <li>mveldhuis@ostrelappraisals.com</li>
    <li>www.ostrelappraisals.com</li>
    <li>Molenvlietkade 27, 4817 KT Leiden The Netherlands</li>
  </ul>
</section>

</body>
</html>
```